Design for social media advertising campaign

Multiple designs to be produced for a legal services advertising campaign in Australia offering assistance to small to medium sized businesses facing financial issues arising from the economic consequences of Covid-19. Designs must be sized suitably for LinkedIn, Twitter and Facebook. See our website recovery.harbourline.example and Facebook page QuillardLaw.CoastAdvisers for logo, colours etc. Examples of the messaging is in the 5 uploaded files.

Target Market(s)

Small / medium size business owners

Industry/Entity Type

Legal

Requirements
Must have
• Sizing for Facebook, LinkedIn and Twitter

```html
<!DOCTYPE html>
<html lang="en">
<head>
<meta charset="utf-8">
<title>Insolvency Campaign – Social Ad</title>
<link rel="stylesheet" href="https://fonts.googleapis.com/css2?family=Poppins:wght@400;500;700;800&family=Montserrat:wght@300&display=swap">
<style>
  :root {
    --page: #ffffff;
    --gold: #a9985e;
    --burgundy: #86181c;
    --burgundy-line: #7a1a1d;
    --navy-deep: #070b18;
    --sky: #c9d6e2;
    --steel: #7d93ab;
    --white: #ffffff;
  }
  * { margin: 0; padding: 0; box-sizing: border-box; }
  html, body {
    width: 1200px; height: 1000px; overflow: hidden;
    background: var(--page);
  }
  .ad-card {
    position: absolute; left: 130px; top: 33px;
    width: 932px; height: 933px;
    overflow: hidden;
    box-shadow: 0 4px 26px rgba(0,0,0,0.12);
  }
  .accent-strip {
    position: absolute; left: 0; top: 0; width: 15px; height: 100%;
    background: var(--gold); z-index: 3;
  }
  .hero-photo {
    position: absolute; inset: 0 0 0 15px;
    background:
      linear-gradient(180deg, rgba(7,11,24,0) 40%, rgba(12,18,40,0.85) 70%, var(--navy-deep) 100%),
      linear-gradient(100deg, #8c8f94 0%, #3b4766 22%, #2a3558 40%, var(--steel) 62%, var(--sky) 100%);
  }
  .firm-tag {
    position: absolute; right: 0; top: 37px;
    width: 457px; height: 116px;
    background: var(--gold); color: var(--white);
    font-family: "Poppins", sans-serif; font-weight: 400;
    font-size: 30px; line-height: 37px;
    text-align: center; padding-top: 20px; z-index: 2;
    white-space: nowrap;
  }
  .headline {
    position: absolute; left: 15px; right: 0; top: 487px;
    text-align: center; color: var(--white); z-index: 2;
    font-family: "Poppins", sans-serif;
  }
  .headline-lead {
    font-weight: 700; font-size: 52px; line-height: 62px;
    letter-spacing: -0.5px;
  }
  .headline-key {
    display: inline-block; margin-top: 14px;
    width: 486px; height: 91px;
    border: 5px solid var(--burgundy-line);
    font-family: "Montserrat", sans-serif; font-weight: 300;
    font-size: 60px; line-height: 80px;
    margin-left: -16px; padding-left: 22px;
    white-space: nowrap;
  }
  .headline-close {
    font-weight: 800; font-size: 64px; line-height: 76px;
    letter-spacing: 1px; margin-top: -4px;
  }
  .offer {
    position: absolute; left: 15px; right: 0; top: 768px;
    text-align: center; color: var(--white); z-index: 2;
    font-family: "Poppins", sans-serif; font-weight: 500; font-size: 24px;
  }
  .cta-button {
    position: absolute; left: 357px; top: 814px;
    width: 226px; height: 73px;
    background: var(--burgundy); color: var(--white);
    border-radius: 3px; z-index: 2;
    font-family: "Poppins", sans-serif; font-weight: 500;
    font-size: 40px; line-height: 73px; text-align: center;
  }
</style>
</head>
<body>
  <div class="ad-card">
    <div class="accent-strip"></div>
    <div class="hero-photo" role="img" aria-label="Photo of a worried young businessman in a navy suit leaning against a wall in a glass-arched walkway overlooking city towers"></div>
    <div class="firm-tag">Swanport Recovery Lawyers<br>(08) 5550 0199</div>
    <div class="headline">
      <div class="headline-lead">Is your business</div>
      <div class="headline-key">STRUCTURED</div>
      <div class="headline-close">TO SURVIVE?</div>
    </div>
    <div class="offer">obtain our free guide</div>
    <div class="cta-button">NOW</div>
  </div>
</body>
</html>
```